Environmental Plastics Infographic on Marine Debris

We need a series of infographics that can be used individually or as a combined presentation. We'd like the combined piece to include an introduction and conclusion along with 4-5 infographics. Each infographic (information unit) should also work as a standalone. We are trying to help people visualize size proportions and ratios to put the plastics marine debris problem in perspective. Our key point is concerning polystyrene foam which represents 35 tons. We are looking for something creative to help people understand what the problem represents in terms they are familiar with.

To view our typical company design/style please see our website at www.brantleyfoamworks.org. Our primary RGB colors are: (187,140,9); (94,47,29); (94,138,164); and (164,167,15). Secondary RGB colors are (249,162,28) and (218,210,208). Our title/header font is DIN Next LT Pro and our copy font is Calibri 10.5 pt. We can deviate from the font specification if beneficial and welcome interesting text treatments and typography.

Need extra days to review

Target Market(s)

international brand manufacturers (corvantel, makiro), US legislators & government agencies

Font styles to use
Sans Serif

Requirements
Must have
• Sufficient white space. Easy to grasp message concept with visual components.

```html
<!DOCTYPE html>
<html lang="en">
<head>
<meta charset="utf-8">
<title>How Big is BIG? – Plastics in the Garbage Patch</title>
<link rel="stylesheet" href="https://fonts.googleapis.com/css2?family=Open+Sans:wght@300;400;600;700;800&display=swap">
<style>
  :root {
    --sand: #dad2d0;
    --sand-light: #efebea;
    --stone: #b7aeac;
    --ink: #0d2b3a;
    --ocean-deep: #2a5673;
    --ocean: #5e8aa4;
    --ocean-mist: #a9b9c4;
    --amber: #f9a21c;
    --rust: #e8731a;
    --flame: #e4571b;
    --white: #ffffff;
  }
  html, body {
    margin: 0;
    padding: 0;
    width: 1200px;
    height: 913px;
    overflow: hidden;
    background: var(--white);
    font-family: "Open Sans", sans-serif;
  }
  .canvas { position: relative; width: 1200px; height: 913px; }
  .panel { position: absolute; width: 538px; height: 404px; }
  .panel svg { display: block; width: 100%; height: 100%; }
  .panel--composition { left: 27px; top: 37px; }
  .panel--comparison  { left: 636px; top: 37px; }
  .panel--weights     { left: 332px; top: 473px; }

  .copy { font-family: "Open Sans", sans-serif; fill: var(--ink); }
  .copy--lead { font-size: 27px; font-weight: 400; }
  .copy--lead-strong { font-weight: 700; }
  .copy--body { font-size: 17.5px; }
  .stat { font-weight: 700; fill: var(--rust); font-size: 42px; }
  .stat-tail { font-size: 17.5px; fill: var(--ink); font-weight: 400; }
  .leader { fill: none; stroke: var(--ink); stroke-width: 3; }
  .marker { fill: none; stroke: var(--ocean-deep); stroke-width: 6; }

  .title { font-size: 46px; font-weight: 700; fill: var(--ink); }
  .column-label { font-size: 20px; font-weight: 700; fill: var(--rust); }
  .column-sub { font-size: 14px; font-weight: 700; fill: var(--rust); }
  .share { font-size: 58px; font-weight: 800; fill: var(--flame); }
  .share-unit { font-size: 33px; font-weight: 300; fill: var(--rust); letter-spacing: 1px; }

  .card-label { font-size: 18px; fill: var(--ink); }
  .card-sub { font-size: 12.5px; fill: var(--ink); }
  .card-number { font-size: 26px; font-weight: 700; fill: var(--ink); }
  .card-unit { font-size: 25px; fill: var(--ink); }
  .connector { stroke: var(--sand-light); stroke-width: 5; fill: none; }
  .weight-value { font-size: 24px; font-weight: 400; fill: var(--sand); }
  .weight-unit { font-size: 9px; fill: var(--sand); }
</style>
</head>
<body>
<main class="canvas">

  <!-- Composition of plastics mass -->
  <section class="panel panel--composition">
    <svg viewBox="0 0 794 596" aria-labelledby="composition-title">
      <defs>
        <linearGradient id="sea-composition" x1="0" y1="1" x2="1" y2="0">
          <stop offset="0" stop-color="var(--ocean-deep)"/>
          <stop offset="1" stop-color="var(--ocean)"/>
        </linearGradient>
      </defs>
      <rect width="794" height="596" fill="var(--sand)"/>
      <path d="M0,500 C200,495 320,455 420,400 C540,330 650,285 794,282 L794,596 L0,596 Z" fill="var(--ocean-mist)"/>
      <path d="M0,516 C210,512 330,470 430,415 C550,348 660,300 794,298 L794,596 L0,596 Z" fill="url(#sea-composition)"/>

      <text id="composition-title" class="copy copy--lead" text-anchor="end">
        <tspan x="346" y="51">The total plastics mass in</tspan>
        <tspan x="346" y="88">the GPGP is projected at</tspan>
        <tspan x="346" y="124" class="copy--lead-strong">78,908 tons</tspan>
      </text>

      <!-- pie chart quadrants -->
      <g class="pie">
        <path d="M503,288 L503,86 A202,202 0 0 0 301,288 Z" fill="var(--amber)" stroke="var(--rust)" stroke-width="4"/>
        <path d="M503,296 L301,296 A202,202 0 0 0 503,498 Z" fill="var(--amber)" stroke="var(--rust)" stroke-width="4"/>
        <path d="M511,296 L511,498 A202,202 0 0 0 713,296 Z" fill="var(--amber)" stroke="var(--rust)" stroke-width="4"/>
        <g role="img" aria-label="Fishing rod, line and hook illustration">
          <rect x="352" y="108" width="146" height="162" rx="14" fill="var(--ink)" opacity="0.18"/>
        </g>
        <g role="img" aria-label="Plastic jugs and bottles illustration">
          <rect x="352" y="316" width="120" height="118" rx="14" fill="var(--ink)" opacity="0.18"/>
        </g>
        <g role="img" aria-label="Foam cup illustration">
          <rect x="548" y="328" width="86" height="118" rx="12" fill="var(--ink)" opacity="0.18"/>
        </g>
      </g>

      <!-- callout: fishing gear -->
      <polyline class="leader" points="340,211 290,211 290,259 45,259"/>
      <circle class="marker" cx="357" cy="211" r="16"/>
      <text class="copy" text-anchor="middle">
        <tspan x="140" y="201"><tspan class="stat">52%</tspan><tspan class="stat-tail"> is mostly</tspan></tspan>
        <tspan x="140" y="224" class="copy--body">abandoned fishing gear;</tspan>
        <tspan x="140" y="247" class="copy--body">not consumer plastics</tspan>
      </text>

      <!-- callout: foamed plastics -->
      <polyline class="leader" points="532,224 685,224 685,308"/>
      <circle class="marker" cx="685" cy="324" r="16"/>
      <text class="copy" text-anchor="middle">
        <tspan x="608" y="74" class="stat">0.05%</tspan>
        <tspan x="608" y="97" class="copy--body">is foamed plastics,</tspan>
        <tspan x="608" y="121" class="copy--body">including</tspan>
        <tspan x="608" y="144" class="copy--body">polystyrene,</tspan>
        <tspan x="608" y="168" class="copy--body">making it a minor</tspan>
        <tspan x="608" y="192" class="copy--body">component of the</tspan>
        <tspan x="608" y="215" class="copy--body">GPGP</tspan>
      </text>

      <!-- callout: hard plastics -->
      <polyline class="leader" points="462,461 337,461 337,484 45,484"/>
      <circle class="marker" cx="478" cy="461" r="16"/>
      <text class="copy" text-anchor="middle">
        <tspan x="150" y="401"><tspan class="stat">47%</tspan><tspan class="stat-tail"> is hard plastics,</tspan></tspan>
        <tspan x="149" y="425" class="copy--body">sheets, and film,</tspan>
        <tspan x="149" y="449" class="copy--body">making up the majority of</tspan>
        <tspan x="149" y="472" class="copy--body">microplastics mass</tspan>
      </text>
    </svg>
  </section>

  <!-- Size comparison -->
  <section class="panel panel--comparison">
    <svg viewBox="0 0 794 596" aria-labelledby="comparison-title">
      <defs>
        <linearGradient id="sea-comparison" x1="0" y1="0" x2="1" y2="0">
          <stop offset="0" stop-color="var(--ocean)"/>
          <stop offset="1" stop-color="var(--ocean-deep)"/>
        </linearGradient>
        <linearGradient id="scene-tone" x1="0" y1="0" x2="0" y2="1">
          <stop offset="0" stop-color="var(--stone)"/>
          <stop offset="1" stop-color="#5a7f97"/>
        </linearGradient>
      </defs>
      <rect width="794" height="596" fill="var(--sand)"/>
      <path d="M0,272 C70,420 220,540 420,548 C590,552 700,505 794,466 L794,596 L0,596 Z" fill="var(--ocean-mist)"/>
      <path d="M0,296 C75,432 225,555 420,564 C590,568 700,522 794,484 L794,596 L0,596 Z" fill="url(#sea-comparison)"/>

      <text id="comparison-title" class="title" x="397" y="98" text-anchor="middle">How Big is BIG?</text>

      <g class="column">
        <g role="img" aria-label="Cruise ship illustration"><rect x="104" y="135" width="187" height="89" fill="url(#scene-tone)"/></g>
        <rect x="104" y="226" width="187" height="65" fill="var(--sand-light)"/>
        <rect x="104" y="291" width="187" height="305" fill="var(--stone)" opacity="0.8"/>
        <text class="column-label" x="197" y="265" text-anchor="middle">ONE CRUISE SHIP</text>
        <text class="share" x="197" y="386" text-anchor="middle">79%</text>
        <text class="share-unit" x="197" y="421" text-anchor="middle">GPGP</text>
      </g>
      <g class="column">
        <g role="img" aria-label="Blue whale illustration"><rect x="304" y="135" width="187" height="89" fill="url(#scene-tone)"/></g>
        <rect x="304" y="226" width="187" height="65" fill="var(--sand-light)"/>
        <rect x="304" y="291" width="187" height="305" fill="var(--stone)" opacity="0.8"/>
        <text class="column-label" x="397" y="265" text-anchor="middle">ONE BLUE WHALE</text>
        <text class="share" x="397" y="386" text-anchor="middle">53%</text>
        <text class="share-unit" x="397" y="421" text-anchor="middle">GPGP</text>
      </g>
      <g class="column">
        <g role="img" aria-label="Garbage truck and city skyline illustration"><rect x="503" y="135" width="187" height="89" fill="url(#scene-tone)"/></g>
        <rect x="503" y="226" width="187" height="65" fill="var(--sand-light)"/>
        <rect x="503" y="291" width="187" height="305" fill="var(--stone)" opacity="0.8"/>
        <text class="column-label" x="596" y="258" text-anchor="middle">ONE WEEK</text>
        <text class="column-sub" x="596" y="278" text-anchor="middle">NYC WASTE GENERATION</text>
        <text class="share" x="596" y="386" text-anchor="middle">29%</text>
        <text class="share-unit" x="596" y="421" text-anchor="middle">GPGP</text>
      </g>
    </svg>
  </section>

  <!-- Tonnage in weights -->
  <section class="panel panel--weights">
    <svg viewBox="0 0 794 596" aria-label="Tonnage comparison shown as 50-ton weights">
      <defs>
        <symbol id="weight" viewBox="0 0 60 86">
          <path d="M15,34 C8,4 52,4 45,34" fill="none" stroke="var(--ink)" stroke-width="10"/>
          <path d="M5,46 C5,28 55,28 55,46 L55,76 Q55,84 47,84 L13,84 Q5,84 5,76 Z" fill="var(--ink)"/>
          <text class="weight-value" x="30" y="67" text-anchor="middle">50</text>
          <text class="weight-unit" x="30" y="77" text-anchor="middle">TONS</text>
        </symbol>
        <clipPath id="sliver-top"><rect x="416" y="140" width="28" height="100"/></clipPath>
        <clipPath id="sliver-left"><rect x="210" y="265" width="12" height="70"/></clipPath>
      </defs>
      <rect width="794" height="596" fill="var(--amber)"/>

      <g class="hexes" fill="var(--sand)">
        <polygon points="285,192 341,95 453,95 509,192 453,289 341,289"/>
        <polygon points="105,294 161,197 273,197 329,294 273,391 161,391"/>
        <polygon points="463,294 519,197 631,197 687,294 631,391 519,391"/>
        <polygon points="285,399 341,302 453,302 509,399 453,496 341,496"/>
      </g>

      <g class="connectors">
        <line class="connector" x1="220" y1="110" x2="402" y2="110"/>
        <line class="connector" x1="657" y1="174" x2="657" y2="264"/>
        <line class="connector" x1="135" y1="330" x2="135" y2="421"/>
        <line class="connector" x1="387" y1="483" x2="572" y2="483"/>
      </g>

      <g class="weights">
        <use href="#weight" x="347" y="150" width="58" height="84"/>
        <use href="#weight" x="404" y="150" width="58" height="84" clip-path="url(#sliver-top)"/>

        <use href="#weight" x="167" y="234" width="38" height="56"/>
        <use href="#weight" x="229" y="234" width="38" height="56"/>
        <use href="#weight" x="167" y="297" width="38" height="56"/>
        <use href="#weight" x="229" y="297" width="38" height="56"/>
        <use href="#weight" x="205" y="266" width="38" height="56" clip-path="url(#sliver-left)"/>

        <use href="#weight" x="517" y="255" width="53" height="78"/>
        <use href="#weight" x="582" y="255" width="53" height="78"/>

        <use href="#weight" x="354" y="342" width="36" height="54"/>
        <use href="#weight" x="401" y="342" width="36" height="54"/>
        <use href="#weight" x="354" y="406" width="36" height="54"/>
        <use href="#weight" x="401" y="406" width="36" height="54"/>
      </g>

      <g class="card">
        <rect x="51" y="49" width="169" height="125" fill="var(--sand-light)"/>
        <text text-anchor="middle">
          <tspan class="card-label" x="135" y="84">All GPGP Plastics</tspan>
          <tspan class="card-number" x="135" y="118">78,908</tspan>
          <tspan class="card-unit" x="135" y="152">TONS</tspan>
        </text>
      </g>
      <g class="card">
        <rect x="572" y="49" width="169" height="125" fill="var(--sand-light)"/>
        <text text-anchor="middle">
          <tspan class="card-label" x="657" y="84">One Cruise Ship</tspan>
          <tspan class="card-number" x="657" y="118">100,000</tspan>
          <tspan class="card-unit" x="657" y="152">TONS</tspan>
        </text>
      </g>
      <g class="card">
        <rect x="51" y="421" width="169" height="125" fill="var(--sand-light)"/>
        <text text-anchor="middle">
          <tspan class="card-label" x="135" y="443">One Week</tspan>
          <tspan class="card-sub" x="135" y="460">NYC Waste Generation</tspan>
          <tspan class="card-number" x="135" y="495">269,230</tspan>
          <tspan class="card-unit" x="135" y="529">TONS</tspan>
        </text>
      </g>
      <g class="card">
        <rect x="572" y="421" width="169" height="125" fill="var(--sand-light)"/>
        <text text-anchor="middle">
          <tspan class="card-label" x="657" y="455">One Blue Whale</tspan>
          <tspan class="card-number" x="657" y="489">200,000</tspan>
          <tspan class="card-unit" x="657" y="523">TONS</tspan>
        </text>
      </g>
    </svg>
  </section>

</main>
</body>
</html>
```